Merin Dotsworth, Broker Associate

I need a new business card for my Real Estate services. I am a Broker Associate and also have my MBA. I am a PA too. I would like to have it say "Rooted Family Service" too some where. I like the bold look of cards and I think I am leaning towards a black or dark background. I need it to tie in my logo with the Ashgrove Pellman Joel Varick Realty logo. I like the foil and shiny look of some letters too. I might add my picture but would like to see some with out my picture too. I sell a lot of lakefront homes but I don't want it to be focused on water. Maybe subtle?

Target Market(s)

18+

Industry/Entity Type

Real Estate Agent

Contact Information for Business Card

The design must have my logo and Ashgrove Pellman logo.
My name: Merin Dotsworth
My cell phone 555-817-2096
business address: 4260 West Orchard Pike Larkvale, NW 34799
Office phone: 555-670-1382
email: MerinDDotsworth@brelvio.com
website: www.PinewickHomeGuide.com
Facebook: www.plumbook.com/merinpinewickhomeguide
Also 'Rooted Family Service' and Homewright logo must be on it.

Font styles to use
Sans Serif

Colors
0555a3
000000
ffffff
d3d3d3
3176b5

Requirements
Must have
• I want this to stand out from all the other Realtors. I like bold look. I need it to match my logo and tie in the Ashgrove Pellman logo. I can do front and back on card. The office details can be smaller than my name and information.
Nice to have
• I like the foil look and matte as well. I want something bold that stands out.

```html
<!DOCTYPE html>
<html lang="en">
<head>
<meta charset="utf-8">
<title>Merin Dotsworth – Business Card</title>
<link rel="stylesheet" href="https://fonts.googleapis.com/css2?family=Montserrat:wght@500;600;700&family=Arimo:wght@400;700&display=swap">
<style>
  :root {
    --brand-blue: #0555a3;
    --accent-blue: #3176b5;
    --band-blue: #0a6cc4;
    --ink: #000000;
    --paper: #ffffff;
    --rule: #d3d3d3;
    --text-dark: #2b2b2b;
    --stage: #e9e9e9;
  }
  * { margin: 0; padding: 0; box-sizing: border-box; }
  html, body { width: 1200px; height: 844px; overflow: hidden; }
  body {
    background: var(--stage);
    font-family: "Arimo", Arial, sans-serif;
    position: relative;
  }
  .card {
    position: absolute;
    top: 272px;
    width: 520px;
    height: 300px;
    overflow: hidden;
    box-shadow: 0 6px 18px rgba(0,0,0,.18);
  }

  /* Front */
  .card-front { left: 50px; background: var(--paper); }
  .front-logo {
    position: absolute; right: 36px; top: 46px;
    display: flex; align-items: center; gap: 10px;
  }
  .logo-square { width: 14px; height: 14px; background: var(--brand-blue); flex: none; }
  .logo-name {
    font-family: "Montserrat", sans-serif; font-weight: 700;
    font-size: 26px; letter-spacing: .5px; color: var(--brand-blue);
    white-space: nowrap;
  }
  .front-rule { position: absolute; left: 40px; right: 36px; height: 1px; background: var(--rule); }
  .front-rule.r1 { top: 98px; }
  .front-rule.r2 { top: 118px; }
  .agent { position: absolute; left: 40px; top: 150px; }
  .agent-name {
    font-family: "Montserrat", sans-serif; font-weight: 600;
    font-size: 20px; color: var(--brand-blue); letter-spacing: .3px;
  }
  .agent-title { font-size: 14px; color: var(--text-dark); margin-top: 1px; }
  .office-address { position: absolute; left: 40px; top: 206px; font-size: 14px; color: var(--text-dark); }
  .front-rule.r3 { top: 232px; left: 40px; right: 300px; }
  .contact-lines {
    position: absolute; left: 40px; right: 30px; top: 242px;
    font-size: 14px; color: var(--text-dark); line-height: 21px; white-space: nowrap;
  }
  .contact-lines b { color: var(--brand-blue); font-weight: 700; }
  .sep { margin: 0 5px; }

  /* Back */
  .card-back {
    left: 630px;
    background: linear-gradient(160deg, #2a2a2a 0%, #0d0d0d 45%, var(--ink) 100%);
  }
  .back-band {
    position: absolute; left: 0; right: 0; bottom: 0; height: 112px;
    background: var(--band-blue);
  }
  .back-logo {
    position: absolute; left: 40px; top: 72px;
    display: flex; align-items: center; gap: 10px;
  }
  .back-logo .logo-square { background: var(--paper); }
  .back-logo .logo-name { color: var(--paper); font-size: 24px; }
  .tagline {
    position: absolute; left: 40px; top: 136px;
    font-family: "Montserrat", sans-serif; font-weight: 600;
    color: var(--paper); font-size: 14px; letter-spacing: 2px;
  }
  .partner {
    position: absolute; right: 20px; top: 40px; width: 118px; text-align: center;
  }
  .partner-name {
    display: block; font-family: "Montserrat", sans-serif; font-weight: 700;
    font-size: 12px; color: var(--paper); letter-spacing: .5px; line-height: 15px;
  }
  .partner-office {
    display: block; font-size: 10px; color: var(--paper);
    letter-spacing: 1px; margin-top: 4px; line-height: 13px;
  }
  .social {
    position: absolute; left: 40px; bottom: 44px;
    display: flex; align-items: center; gap: 7px;
    color: var(--paper); font-size: 14px;
  }
  .social-dot { width: 12px; height: 12px; border-radius: 50%; background: var(--paper); }
</style>
</head>
<body>
  <section class="card card-front" aria-label="Business card front">
    <div class="front-logo">
      <span class="logo-square"></span>
      <span class="logo-name">MERIN DOTSWORTH</span>
    </div>
    <div class="front-rule r1"></div>
    <div class="front-rule r2"></div>
    <div class="agent">
      <div class="agent-name">MERIN DOTSWORTH</div>
      <div class="agent-title">Broker Associate</div>
    </div>
    <div class="office-address">4260 West Orchard Pike Larkvale, NW 34799</div>
    <div class="front-rule r3"></div>
    <div class="contact-lines">
      <div><b>P:</b> 555-670-1382<span class="sep">|</span><b>M:</b> 555-817-2096</div>
      <div><b>E:</b> MerinDDotsworth@brelvio.com<span class="sep">|</span><b>W:</b> www.PinewickHomeGuide.com</div>
    </div>
  </section>

  <section class="card card-back" aria-label="Business card back">
    <div class="back-band"></div>
    <div class="back-logo">
      <span class="logo-square"></span>
      <span class="logo-name">MERIN DOTSWORTH</span>
    </div>
    <div class="tagline">ROOTED FAMILY SERVICE</div>
    <div class="partner">
      <span class="partner-name">ASHGROVE PELLMAN</span>
      <span class="partner-office">JOEL VARICK<br>REALTY</span>
    </div>
    <div class="social">
      <span class="social-dot"></span>
      <span>www.plumbook.com/merinpinewickhomeguide</span>
    </div>
  </section>
</body>
</html>
```